Innovative Beverage Company needs a Packaging Design/Line Extension

We need a packaging design for a line extension for a new flavour of our beverage line called Vexa. Vexa is a 7% alcohol by volume "cooler" sold in aluminium cans. Its packaging is known for is bright colours and graphic design.

We are looking for a design that will "fit" with our existing product line. To "fit" the design will need to be somewhat different to the current products, but also complimentary in terms of design and chosen colours.

Attached are the current designs that we use, and the die-line.

Target Market(s)

The target demographic are women from 18 to 30.

Industry/Entity Type

It Company

Requirements
Must have
• We are looking for a design that will "fit" with our existing product line. To "fit" the design will need to be somewhat different to the current products, but also complimentary in terms of design and chosen colours.

```html
<!DOCTYPE html>
<html lang="en">
<head>
<meta charset="utf-8">
<title>Vexa Watermelon + Guarana – Can Label</title>
<link rel="stylesheet" href="https://fonts.googleapis.com/css2?family=Comfortaa:wght@400;700&family=Open+Sans:wght@400;700&display=swap">
<style>
  :root{
    --page:#ffffff;
    --panel-blue:#b3e0e7;
    --teal:#2db4be;
    --navy:#1f2b5e;
    --mid-blue:#5a8fd2;
    --sky:#8fd3df;
    --coral:#ef6b4b;
    --ink:#3a3a3a;
    --label-white:#ffffff;
  }
  html,body{margin:0;padding:0;width:1200px;height:760px;overflow:hidden;background:var(--page);}
  .canvas{position:relative;width:1200px;height:760px;}
  .can-label{position:absolute;left:147px;top:29px;width:906px;height:702px;display:block;}
  .display{font-family:"Comfortaa",sans-serif;}
  .body-text{font-family:"Open Sans",sans-serif;}
  .brand-name{font-family:"Comfortaa",sans-serif;font-weight:700;fill:var(--ink);font-size:50px;letter-spacing:1px;}
  .flavour{font-family:"Comfortaa",sans-serif;font-weight:700;fill:var(--coral);font-size:12.5px;}
  .badge-box{fill:var(--coral);}
  .badge-text{font-family:"Open Sans",sans-serif;font-weight:700;fill:#fff;font-size:6px;letter-spacing:.4px;}
  .abv{font-family:"Comfortaa",sans-serif;font-weight:700;fill:var(--ink);font-size:15px;}
  .panel-heading{font-family:"Open Sans",sans-serif;font-weight:700;fill:var(--navy);font-size:7px;letter-spacing:.3px;}
  .panel-copy{font-family:"Open Sans",sans-serif;fill:var(--navy);font-size:5.2px;}
  .web-address{font-family:"Open Sans",sans-serif;font-weight:700;fill:var(--navy);font-size:7px;}
  .fine-print{font-family:"Open Sans",sans-serif;fill:var(--navy);font-size:5.6px;}
  .fine-print .lead{font-weight:700;}
  .band-text{font-family:"Open Sans",sans-serif;fill:#fff;font-size:6.4px;letter-spacing:.5px;}
</style>
</head>
<body>
<main class="canvas">
  <svg class="can-label" viewBox="0 0 625 484" xmlns="http://www.w3.org/2000/svg" aria-labelledby="label-title">
    <title id="label-title">Vexa Watermelon + Guarana can label, flat die-line</title>
    <defs>
      <linearGradient id="pattern-top" x1="0" y1="0" x2="1" y2="1">
        <stop offset="0" stop-color="#4f86cc"/>
        <stop offset=".45" stop-color="#35b3bf"/>
        <stop offset=".8" stop-color="#8fd3df"/>
        <stop offset="1" stop-color="#5a8fd2"/>
      </linearGradient>
      <linearGradient id="pattern-bottom" x1="0" y1="1" x2="1" y2="0">
        <stop offset="0" stop-color="#35b3bf"/>
        <stop offset=".5" stop-color="#5a8fd2"/>
        <stop offset="1" stop-color="#8fd3df"/>
      </linearGradient>
    </defs>

    <!-- label base -->
    <rect class="label-face" x="0" y="0" width="625" height="484" fill="var(--label-white)"/>

    <!-- side information panel -->
    <g class="info-panel">
      <rect x="0" y="0" width="148" height="484" fill="var(--panel-blue)"/>

      <text class="panel-heading" x="74" y="48" text-anchor="middle">SERVIR FROID</text>
      <rect x="10" y="58" width="126" height="52" fill="var(--teal)"/>
      <text class="panel-copy" text-anchor="middle">
        <tspan x="73" y="69">Savourez le goût frais du fruit par</tspan>
        <tspan x="73" y="78">excellence de l'été : le melon</tspan>
        <tspan x="73" y="87">d'eau. Cette boisson vous</tspan>
        <tspan x="73" y="96">rafraîchira de la première à la</tspan>
        <tspan x="73" y="105">dernière gorgée!</tspan>
      </text>

      <text class="panel-heading" x="74" y="124" text-anchor="middle">SERVE CHILLED</text>
      <rect x="10" y="131" width="126" height="37" fill="var(--teal)"/>
      <text class="panel-copy" text-anchor="middle">
        <tspan x="73" y="142">Savour the taste of the ultimate</tspan>
        <tspan x="73" y="151">summer fruit: watermelon. You'll</tspan>
        <tspan x="73" y="160">be sure to enjoy this refreshing</tspan>
        <tspan x="73" y="167.5">drink to the very last drop.</tspan>
      </text>

      <text class="web-address" x="74" y="188" text-anchor="middle">www.drinkvexa.ca</text>

      <g class="fine-print" transform="translate(131,196) rotate(90)">
        <text><tspan class="lead" x="0" y="0">INGRÉDIENTS :</tspan> eau, glucose-fructose, cidre, extrait de guarana,</text>
        <text x="0" y="8.5">saveur naturelle (melon d'eau), acide citrique, sorbate de</text>
        <text x="0" y="17">potassium, métabisulfite de potassium (sulfites).</text>
        <text><tspan class="lead" x="0" y="25.5">INGREDIENTS:</tspan> water, glucose-fructose, cider, guarana extract,</text>
        <text x="0" y="34">natural flavour (watermelon), citric acid, potassium sorbate,</text>
        <text x="0" y="42.5">potassium metabisulphite (sulphites). Caffeine 32 mg / 473 mL.</text>
        <text x="0" y="51">Consignée là où la loi le prévoit. Return for refund where applicable.</text>
        <text x="150" y="68">Produit élaboré au Canada par Boissons Ardoise inc.</text>
        <text x="150" y="76.5">Product made in Canada by Ardoise Beverages inc.</text>
        <text x="150" y="85">120 rue des Érables, Val-Joli (QC) J0A 0A0</text>
      </g>
    </g>

    <!-- decorative block pattern areas -->
    <polygon class="pattern-top" role="img" aria-label="Decorative pattern of stacked hand-drawn squares in teal, navy, blue and coral"
      points="148,0 625,0 625,140 560,124 500,110 440,122 380,150 320,178 262,228 205,258 148,286"
      fill="url(#pattern-top)"/>
    <polygon class="pattern-bottom" role="img" aria-label="Decorative pattern of stacked hand-drawn squares in teal, navy, blue and coral"
      points="148,395 205,372 262,356 330,338 392,322 452,304 520,268 580,238 625,224 625,484 148,484"
      fill="url(#pattern-bottom)"/>

    <!-- front, French -->
    <g class="front-fr">
      <text class="brand-name" x="200" y="270">Vexa</text>
      <text class="flavour" x="206" y="290">Melon d'eau</text>
      <rect class="badge-box" x="206" y="296" width="44" height="10" rx="2"/>
      <text class="badge-text" x="210" y="303">+ GUARANA</text>
      <text class="abv" x="207" y="325">7 % alc./vol.</text>
    </g>

    <!-- front, English -->
    <g class="front-en" transform="rotate(-7 520 190)">
      <text class="brand-name" x="440" y="195">Vexa</text>
      <text class="flavour" x="446" y="215">Watermelon</text>
      <rect class="badge-box" x="446" y="221" width="44" height="10" rx="2"/>
      <text class="badge-text" x="450" y="228">+ GUARANA</text>
      <text class="abv" x="447" y="250">7 % alc./vol.</text>
    </g>

    <!-- bottom band legal line -->
    <text class="band-text" x="178" y="465">BOISSON ALCOOLISÉE ALTERNATIVE  473mL</text>
    <text class="band-text" x="392" y="465">ALTERNATIVE ALCOHOLIC BEVERAGE  473mL</text>
  </svg>
</main>
</body>
</html>
```